Design a menu for health restaurant

A health food restaurant in Los Angeles is seeking menu design. Our foods are made from scratch using whole ingredients.
Name: Grubb Larder
Address: 1000 E 60th StLos Angeles, CA 90247
Website: www.GrubbLarder.example
We are looking for a clean and simple menu. Brand colors are white/tan, green and orange.

Please see attached excel with menu items and logo. We do not yet have prices.

Colors
f78f20
9bcb3c
ffffff
fff3d1

Requirements
Must have
• Easy to read.
Trifold menu design (front and back).
VEGAN, VEGETARIAN, GLUTEN FREE, CONTAINS NUTS symbols.
Logo.
Nice to have
• Incorporate brand colors, but still be easy to read.
We would like to use the Belco font (attached) if it works. If not we are open to a similar font that is easy to read.

Please see attached images.
We like the images and headers of OPTION 1. Would like something similar in trifold format.
We like the clean fonts of OPTION 2.

```html
<!DOCTYPE html>
<html lang="en">
<head>
<meta charset="utf-8">
<title>Grubb Larder Menu</title>
<link href="https://fonts.googleapis.com/css2?family=Montserrat:wght@400;500;600&display=swap" rel="stylesheet">
<style>
:root{
  --orange:#f78f20;
  --green:#9bcb3c;
  --tan:#fff3d1;
  --ink:#1a1a1a;
  --paper:#ffffff;
}
*{margin:0;padding:0;box-sizing:border-box}
html,body{width:1200px;height:934px;overflow:hidden;background:var(--paper)}
body{font-family:"Montserrat",Arial,sans-serif;color:var(--ink);position:relative}
.abs{position:absolute}
.band{position:absolute;height:20px;font-size:17.5px;font-weight:500;line-height:21px;padding-left:19px;letter-spacing:.1px}
.band--orange{background:var(--orange)}
.band--green{background:var(--green)}
.band--tan{background:var(--tan)}
.item-title{position:absolute;font-size:12px;font-weight:600;letter-spacing:.1px;white-space:nowrap;display:flex;align-items:center;gap:6px;line-height:14px}
.price{position:absolute;font-size:12px;font-weight:600;line-height:14px}
.price--right{text-align:right;width:70px}
.desc{position:absolute;font-size:12.3px;line-height:12.6px;font-weight:400;letter-spacing:-.25px;white-space:nowrap}
.icons{display:inline-flex;gap:4px;align-items:center}
.icon{width:18px;height:16px}
.icon-gf{width:19px;height:19px}
.icon-nut{width:26px;height:12px}
.photo{position:absolute;left:803px;top:14px;width:397px;height:616px;
  background:linear-gradient(150deg,#e9e9e6 0%,#c9b08c 35%,#6f8a3c 55%,#d9a56a 75%,#eceae4 100%)}
.brand-mark{position:absolute;left:960px;top:664px;width:56px;height:56px;border-radius:50%;background:var(--orange)}
.brand-name{position:absolute;left:803px;top:730px;width:397px;text-align:center;font-size:22px;font-weight:500;color:var(--orange)}
.contact{position:absolute;left:803px;width:397px;text-align:center;font-size:16.6px;font-weight:400}
</style>
</head>
<body>
<svg width="0" height="0" style="position:absolute">
  <defs>
    <symbol id="leaf" viewBox="0 0 20 16"><path d="M2 15 C6 10 10 7 17 2 C17 9 12 13 6 12 Z M3 9 C5 6 8 6 10 7 C8 9 5 10 3 9Z" fill="#1a1a1a"/><path d="M2 15 L14 5" stroke="#fff" stroke-width="1"/></symbol>
    <symbol id="nut" viewBox="0 0 28 14"><ellipse cx="7" cy="7" rx="6" ry="5" fill="#1a1a1a"/><ellipse cx="14" cy="7" rx="5" ry="5.5" fill="#1a1a1a"/><ellipse cx="21" cy="7" rx="6" ry="5" fill="#1a1a1a"/></symbol>
    <symbol id="gf" viewBox="0 0 20 20"><circle cx="10" cy="10" r="8.8" fill="none" stroke="#1a1a1a" stroke-width="1.2"/><path d="M10 5 V16" stroke="#1a1a1a" stroke-width="1"/><ellipse cx="10" cy="5" rx="1.2" ry="1.8" fill="#1a1a1a"/><ellipse cx="8" cy="8" rx="1.2" ry="1.8" fill="#1a1a1a"/><ellipse cx="12" cy="8" rx="1.2" ry="1.8" fill="#1a1a1a"/><ellipse cx="8" cy="11.5" rx="1.2" ry="1.8" fill="#1a1a1a"/><ellipse cx="12" cy="11.5" rx="1.2" ry="1.8" fill="#1a1a1a"/></symbol>
  </defs>
</svg>

<section class="panel panel--left">
  <div class="band band--orange" style="left:13px;top:29px;width:279px">BURGERS N' SAMMIES</div>

  <div class="item-title" style="left:32px;top:73px">AIR FRIED CHICKEN SAMMY</div>
  <div class="price" style="left:348px;top:73px">$11.99</div>
  <p class="desc" style="left:32px;top:94px">Air fried chicken breast topped with red leaf lettuce, tomato,<br>house made pickles and Larder Sauce on a bun served<br>with choice of salad of fries.</p>

  <div class="item-title" style="left:32px;top:147px">GRILLED CHICKEN SAMMY</div>
  <div class="price" style="left:348px;top:147px">$11.99</div>
  <p class="desc" style="left:32px;top:168px">Grilled chicken topped with guacamole, red leaf lettuce,<br>tomato, house made pickles and Larder Sauce. Served<br>with regular fries or side salad.</p>

  <div class="item-title" style="left:32px;top:221px">CLASSIC BEEF BURGER</div>
  <div class="price" style="left:348px;top:221px">$11.99</div>
  <p class="desc" style="left:32px;top:242px">House seasoned beef burger topped with red leaf lettuce,<br>tomato, cheddar cheese, house made pickles and Larder<br>Sauce on a bun served with choice of salad of fries.</p>

  <div class="item-title" style="left:32px;top:294px">BLACK BEAN PINE NUT BURGER
    <span class="icons"><svg class="icon"><use href="#leaf"/></svg><svg class="icon-nut"><use href="#nut"/></svg></span></div>
  <div class="price" style="left:348px;top:295px">$11.99</div>
  <p class="desc" style="left:32px;top:316px">House made black bean pine nut burger topped with red<br>leaf lettuce, tomato, house made pickles and mustard aioli<br>on a bun served with choice of salad of fries.</p>

  <div class="item-title" style="left:32px;top:366px">SALMON BURGER</div>
  <div class="price" style="left:348px;top:364px">$11.99</div>
  <p class="desc" style="left:32px;top:389px">House made salmon burger topped with red leaf lettuce,<br>tomato, house made pickles and Larder yogurt on a bun<br>served with choice of salad of fries.</p>

  <div class="band band--green" style="left:13px;top:461px;width:276px">SNACKS N' SIDES</div>

  <div class="item-title" style="left:32px;top:494px">FRIES <span class="icons"><svg class="icon"><use href="#leaf"/></svg><svg class="icon-gf"><use href="#gf"/></svg></span></div>
  <p class="desc" style="left:32px;top:516px">Hand cut air-fries with<br>house seasonings.<br>Choose regular or sweet<br>potato fries.</p>
  <div class="price" style="left:32px;top:575px">$11.99</div>

  <div class="item-title" style="left:228px;top:495px">SIDE SALAD</div>
  <p class="desc" style="left:228px;top:516px">Your choice of House,<br>Golden Beet,<br>Mediterranean, or Vegan<br>Chef side salad. (24oz)</p>
  <div class="price" style="left:228px;top:575px">$11.99</div>

  <div class="item-title" style="left:32px;top:605px">GUAC + CHIPS <span class="icons"><svg class="icon"><use href="#leaf"/></svg><svg class="icon-gf"><use href="#gf"/></svg></span></div>
  <p class="desc" style="left:32px;top:629px">Guacamole with blue corn<br>tortilla chips.</p>
  <div class="price" style="left:32px;top:662px">$11.99</div>

  <div class="item-title" style="left:228px;top:605px">HUMMUS + CHIPS <span class="icons"><svg class="icon"><use href="#leaf"/></svg><svg class="icon-gf"><use href="#gf"/></svg></span></div>
  <p class="desc" style="left:228px;top:629px">Hummus with blue corn<br>tortilla chips.</p>
  <div class="price" style="left:228px;top:662px">$11.99</div>

  <div class="band band--tan" style="left:13px;top:711px;width:276px">COMBOS</div>

  <div class="item-title" style="left:32px;top:744px">SOUP + SALAD</div>
  <p class="desc" style="left:32px;top:766px">Your choice of soup and<br>side salad.<br>16oz soup + 38oz salad</p>
  <div class="price" style="left:32px;top:813px">$11.99</div>

  <div class="item-title" style="left:228px;top:744px">AVO TOAST COMBO</div>
  <p class="desc" style="left:228px;top:766px">Half avocado toast and<br>your choice of soup. 16oz</p>
  <div class="price" style="left:228px;top:813px">$11.99</div>

  <div class="item-title" style="left:32px;top:851px">SOUP + SAMMY</div>
  <div class="price" style="left:348px;top:851px">$11.99</div>
  <p class="desc" style="left:32px;top:873px">Your choice of soup and sandwich.<br>16oz soup + Sandwich</p>
</section>

<section class="panel panel--middle">
  <div class="band band--orange" style="left:402px;top:29px;width:289px">DESSERTS</div>

  <div class="item-title" style="left:417px;top:62px">DATE COFFEE CAKE</div>
  <span class="abs icons" style="left:418px;top:80px"><svg class="icon"><use href="#leaf"/></svg><svg class="icon-nut"><use href="#nut"/></svg></span>
  <p class="desc" style="left:417px;top:104px">Signature date coffee cake<br>with walnuts.</p>
  <div class="price" style="left:417px;top:143px">$11.99</div>

  <div class="item-title" style="left:616px;top:62px">FRUIT + SPICES</div>
  <span class="abs icons" style="left:616px;top:78px"><svg class="icon"><use href="#leaf"/></svg><svg class="icon-gf"><use href="#gf"/></svg></span>
  <p class="desc" style="left:616px;top:104px">Strawberry, pineapple,<br>green apple, orange, and<br>blueberries with lime and<br>chili seasoning.</p>
  <div class="price" style="left:616px;top:163px">$11.99</div>

  <div class="item-title" style="left:418px;top:192px">COOKIES</div>
  <span class="abs icons" style="left:419px;top:211px"><svg class="icon"><use href="#leaf"/></svg></span>
  <p class="desc" style="left:418px;top:235px">Your choice of Chocolate<br>Chip or Double Chocolate<br>Chip fresh baked cookie.</p>
  <div class="price" style="left:418px;top:283px">$11.99</div>

  <div class="item-title" style="left:617px;top:192px;white-space:normal;width:160px;line-height:12.6px">LARDER CHOCOLATE MOUSSE</div>
  <span class="abs icons" style="left:617px;top:220px"><svg class="icon"><use href="#leaf"/></svg><svg class="icon-gf"><use href="#gf"/></svg></span>
  <p class="desc" style="left:617px;top:247px">Served with grated dark<br>chocolate.</p>
  <div class="price" style="left:617px;top:283px">$11.99</div>

  <div class="band band--green" style="left:402px;top:322px;width:289px">DRINKS</div>

  <div class="item-title" style="left:417px;top:361px">COFFEE</div>
  <div class="price price--right" style="left:699px;top:361px">$11.99</div>
  <p class="desc" style="left:417px;top:383px">We proudly serve Alderwood Coffee, a local roaster.</p>

  <div class="item-title" style="left:417px;top:414px">POWER DATE SHAKE <span class="icons"><svg class="icon"><use href="#leaf"/></svg><svg class="icon-gf"><use href="#gf"/></svg></span></div>
  <div class="price price--right" style="left:699px;top:416px">$11.99</div>
  <p class="desc" style="left:417px;top:439px">Ice-blended energy smoothie featuring dates and coffee.</p>

  <div class="item-title" style="left:417px;top:466px">HEART BEET JUICE <span class="icons"><svg class="icon"><use href="#leaf"/></svg><svg class="icon-gf"><use href="#gf"/></svg></span></div>
  <div class="price price--right" style="left:699px;top:468px">$11.99</div>
  <p class="desc" style="left:417px;top:491px">Red beet, apple, carrot, ginger, parsley, and lemon.</p>

  <div class="item-title" style="left:417px;top:516px">GREEN LEAFY JUICE <span class="icons"><svg class="icon"><use href="#leaf"/></svg><svg class="icon-gf"><use href="#gf"/></svg></span></div>
  <div class="price price--right" style="left:699px;top:518px">$11.99</div>
  <p class="desc" style="left:417px;top:541px">Spinach, kale, cucumber, apple, and oranges.</p>

  <div class="item-title" style="left:417px;top:568px">ORANGE TURMERIC JUICE <span class="icons"><svg class="icon"><use href="#leaf"/></svg><svg class="icon-gf"><use href="#gf"/></svg></span></div>
  <div class="price price--right" style="left:699px;top:570px">$11.99</div>
  <p class="desc" style="left:417px;top:594px">Turmeric, ginger, lemon, carrot, and orange topped with<br>cracked black pepper.</p>

  <div class="item-title" style="left:417px;top:628px">FIRESHOT <span class="icons"><svg class="icon"><use href="#leaf"/></svg><svg class="icon-gf"><use href="#gf"/></svg></span></div>
  <div class="price price--right" style="left:699px;top:631px">$11.99</div>
  <p class="desc" style="left:417px;top:654px">Ginger and lemon shot topped with cayenne.</p>

  <div class="item-title" style="left:417px;top:678px">LEMONADE</div>
  <div class="price price--right" style="left:699px;top:678px">$11.99</div>
  <p class="desc" style="left:417px;top:701px">House Made Lemonade. Choice of unsweetened or agave<br>sweetened in Regular, Raspberry, and Lavender flavors.</p>

  <div class="item-title" style="left:417px;top:740px">TEA</div>
  <div class="price price--right" style="left:699px;top:740px">$11.99</div>
  <p class="desc" style="left:417px;top:763px">Hot or iced.</p>

  <div class="item-title" style="left:417px;top:792px">BOTTLED DRINKS</div>
  <div class="price price--right" style="left:699px;top:792px">$11.99</div>
  <p class="desc" style="left:417px;top:816px">Brightleaf kombucha (Sunrise Blend, Ginger Bramble,<br>Mango Glow)<br>Driftwell (Orange Mango, Lemon, Grapefruit)<br>Palmera Classic<br>Sparkling Water (Everspring)<br>Still Water (Everspring)</p>
</section>

<section class="panel panel--right">
  <div class="photo" role="img" aria-label="Photo of a grilled chicken salad bowl with blue corn chips and hummus, and a chicken sandwich with slaw"></div>
  <div class="brand-mark"></div>
  <div class="brand-name">Grubb Larder</div>
  <div class="contact" style="top:834px">2417 W 83rd St Los Angeles, CA 90247</div>
  <div class="contact" style="top:869px">www.GrubbLarder.example</div>
</section>
</body>
</html>
```